INSTAGRAM STORY FEED FOR LUXURY JEWELRY STORE

For a luxury jewelry retailer. We want to create a set of posts for feed for the post-covid world once we reopen. Our goal is to emphasize the rebirth, the beggining of a new day, with focuses on the REAL important things in life: LOVE (through an engagement rings). LIFE (through baby birth gifts). HAPINESS (through benchmark moments like anniversaries).
Colors must be elegant but happy.
for refference our company Instagram is @vondemi_official so you can have a feel of our brand and product.

Target Market(s)

ENGAGEMENT RINGS. DIAMOND CUSTOMERS. LUXURY RETAIL. LATIN AMERICA.

Industry/Entity Type

Jewelry

Font styles to use
Other font styles liked:
• Our logo uses AUDREY

Requirements
Must have
• THEME MUST BE BASED ON A NEW DAY. ELEGANT COLOR SCHEME, WITH LIGHT COLORS, MUST INCLUDE SEVERAL POSTS FOR INSTAGRAM FEED INCLUDING:
Our goal is to emphasize the rebirth, the beggining of a new day, with focuses on the REAL important things in life: LOVE (through an engagement rings). LIFE (through baby birth gifts). HAPINESS (through benchmark moments like anniversaries).
Nice to have
• CLEAN LOOK. PLEASE VIEW IMAGE EXAMPLES OF THINGS I LIKE.
I HAVE POSTED A “LOVE” SIGN IN IMAGES. It would be nice to make something like that sign, in black font, and white, light grey, or even yellow background, and have a ring or piece of jewelrry balancing or hanging from
One of the letters. Then do something similar with word Life, etc.
Should not have
• NO BLACK. NO DARK COLORS. NOTHING THAT WILL LOOK TACKY.

```html
<!DOCTYPE html>
<html lang="en">
<head>
<meta charset="utf-8">
<title>Vondemi – Begin Your Story Story Post</title>
<link rel="stylesheet" href="https://fonts.googleapis.com/css2?family=Marcellus&display=swap">
<style>
  :root {
    --page-bg: #a6dce8;
    --sun-top: #d9a23c;
    --sun-mid: #f2c35e;
    --sun-glow: #fff2c4;
    --field-dark: #9a6a2c;
    --headline: #e63c1c;
    --brand-white: #ffffff;
    --silver-light: #e4e4e4;
    --silver-dark: #bdbdbd;
    --heart-gold-light: #f3b64a;
    --heart-gold-dark: #dc9226;
    --heart-edge: #e63c1c;
    --pill-red: #e63c1c;
    --url-ink: #2f2f2f;
    --ring-silver: #f4f4f4;
  }
  * { margin: 0; padding: 0; box-sizing: border-box; }
  html, body {
    width: 1200px;
    height: 1040px;
    overflow: hidden;
    background: var(--page-bg);
  }
  body {
    display: flex;
    align-items: center;
    justify-content: center;
    font-family: "Marcellus", serif;
  }
  .story {
    position: relative;
    width: 560px;
    height: 996px;
    overflow: hidden;
    box-shadow: 0 6px 18px rgba(0, 0, 0, 0.18);
  }
  .story__photo {
    position: absolute;
    inset: 0 0 200px 0;
    background:
      radial-gradient(ellipse 60% 35% at 50% 66%, var(--sun-glow) 0%, rgba(255, 242, 196, 0) 70%),
      linear-gradient(180deg, var(--sun-top) 0%, var(--sun-mid) 35%, #f7d98a 60%, #e7b25a 85%, var(--field-dark) 100%);
  }
  .story__band {
    position: absolute;
    left: 0;
    right: 0;
    bottom: 0;
    height: 222px;
    background: linear-gradient(160deg, var(--silver-light) 0%, var(--silver-dark) 55%, var(--silver-light) 100%);
  }
  .brand {
    position: absolute;
    top: 84px;
    left: 0;
    right: 0;
    text-align: center;
    color: var(--brand-white);
    font-size: 44px;
    letter-spacing: 0.32em;
    padding-left: 0.32em;
  }
  .headline {
    position: absolute;
    top: 178px;
    left: 0;
    right: 0;
    text-align: center;
    color: var(--headline);
    font-weight: 400;
    line-height: 1;
  }
  .headline__line {
    display: block;
    font-size: 42px;
    margin-bottom: 12px;
  }
  .headline__line--strong {
    font-size: 46px;
    font-weight: 700;
    letter-spacing: 0.01em;
  }
  .heart {
    position: absolute;
    left: 112px;
    top: 642px;
    width: 338px;
    height: 310px;
  }
  .ring {
    position: absolute;
    left: 246px;
    top: 722px;
    width: 76px;
    height: 188px;
    border-radius: 38px;
    background: radial-gradient(ellipse at 50% 40%, var(--ring-silver) 0%, #d6d6d6 70%, rgba(214, 214, 214, 0) 100%);
  }
  .cta {
    position: absolute;
    left: 35px;
    top: 878px;
    width: 146px;
    height: 28px;
    border-radius: 14px;
    background: var(--pill-red);
    color: #ffffff;
    font-size: 17px;
    letter-spacing: 0.04em;
    display: flex;
    align-items: center;
    justify-content: center;
  }
  .url {
    position: absolute;
    left: 27px;
    top: 916px;
    color: var(--url-ink);
    font-size: 29px;
  }
</style>
</head>
<body>
  <main class="story">
    <div class="story__photo" role="img" aria-label="Sunset photo of a couple embracing in a golden field with doodled hearts above them"></div>
    <div class="story__band"></div>

    <div class="brand">VONDEMI</div>

    <h1 class="headline">
      <span class="headline__line">BEGIN YOUR STORY</span>
      <span class="headline__line">WITH A</span>
      <span class="headline__line headline__line--strong">FABULOUS EXAMPLE</span>
    </h1>

    <svg class="heart" viewBox="0 0 338 310" aria-hidden="true">
      <defs>
        <linearGradient id="heartGold" x1="0" y1="0" x2="1" y2="1">
          <stop offset="0" stop-color="var(--heart-gold-light)"/>
          <stop offset="1" stop-color="var(--heart-gold-dark)"/>
        </linearGradient>
      </defs>
      <path d="M169 52 C138 -6 2 4 8 114 C14 196 118 246 169 306 C220 246 324 196 330 114 C336 4 200 -6 169 52 Z"
            fill="url(#heartGold)" stroke="var(--heart-edge)" stroke-width="7"/>
      <path d="M169 58 C140 4 12 12 14 114" fill="none" stroke="#ffffff" stroke-width="3"/>
      <path d="M169 58 C198 4 326 12 324 114" fill="none" stroke="#ffffff" stroke-width="3"/>
    </svg>

    <div class="ring" role="img" aria-label="Photo of a diamond solitaire engagement ring in white gold"></div>

    <div class="cta">SHOP NOW</div>
    <div class="url">vondemi.com.pa</div>
  </main>
</body>
</html>
```